Enhance the web site presence of Kolrith Global Limited

Upgrade the current web site www.kolrithpanel.com to share with the audience our current plan and future developments of our company. I have created a worksheet which shows all the pages that I like to have. The home page in English, Japanese and Chinese is hyperlinked to the various pages. Under the product, we should allow the user to select "single sided PCB or double sided PCB". The translation of the contents of the pages with Japanese is not complete but the English and Chinese are complete. You can download the briefing and photos in the dropbox files below;

https://www.sharelocker.net/sh/xk4trw92mpd3ab1/BBQm_Lp841zzPq2Rw7KtYnHjEa?dl=0

Target Market(s)

Electronic companies

Industry/Entity Type

Electronic

Coding

Coded - Design and coding required

Number of Pages Required

5+ page

Font styles to use
Sans Serif

Colors
00a990
0353a1
33b8a4

Requirements
Must have
• Get a sense of confidence on our company's integrity and capability to deliver the highest quality PCBs with the most competitive prices and best services. A sense of elegance is essential as we DON'T treat profits as the number one goal. Our number goal is to do the RIGHT things right. Having a mixture of our company photos will be appropriate.

```html
<!DOCTYPE html>
<html lang="en">
<head>
<meta charset="utf-8">
<title>Kolrith Global Limited</title>
<link rel="stylesheet" href="https://fonts.googleapis.com/css2?family=Poppins:wght@300;400;500;600;700&display=swap">
<style>
:root{
  --green:#00a990;
  --teal:#33b8a4;
  --blue:#0353a1;
  --ink:#1d2430;
  --muted:#6b7380;
  --line:#e3e6ea;
  --white:#ffffff;
}
*{box-sizing:border-box;margin:0;padding:0}
html,body{width:1200px;height:3060px;overflow:hidden}
body{font-family:'Poppins',sans-serif;color:var(--ink);background:var(--white);position:relative}
.wrap{position:absolute;left:100px;width:1000px}

/* header */
.topbar{position:absolute;top:0;left:0;width:1200px;height:80px;background:var(--white);z-index:2}
.brand{position:absolute;left:100px;top:18px;display:flex;align-items:center;gap:10px}
.brand-square{width:14px;height:14px;background:var(--blue)}
.brand-name{font-size:30px;font-weight:700;color:var(--blue);letter-spacing:1px}
.contact-strip{position:absolute;right:100px;top:26px;display:flex;gap:26px;font-size:14px;color:var(--ink);align-items:center}
.contact-strip span{display:flex;align-items:center;gap:8px}
.contact-strip svg{width:16px;height:16px;fill:var(--green)}
.lang-dot{width:18px;height:18px;border-radius:50%;background:var(--blue);display:inline-block}
.hero{position:absolute;top:80px;left:0;width:1200px;height:580px;background:linear-gradient(180deg,#c9d3cf 0%,#9fb0a8 35%,#7b8f86 70%,#b9c2bd 100%)}
.navbar{position:absolute;top:96px;left:100px;width:1000px;height:42px;background:var(--green);display:flex;align-items:center;z-index:3}
.navbar a{color:var(--white);font-size:12px;font-weight:500;text-decoration:none;padding:0 18px;height:42px;line-height:42px}
.navbar a.active{background:rgba(0,0,0,.15)}
.navbar .quote{margin-left:auto;background:var(--blue);padding:0 22px}
.hero-title{position:absolute;top:340px;left:0;width:1200px;text-align:center;color:var(--white);font-size:40px;font-weight:600;line-height:1.25;z-index:2;text-shadow:0 2px 6px rgba(0,0,0,.25)}
.hero-arrow{position:absolute;top:300px;width:34px;height:34px;background:var(--white);display:flex;align-items:center;justify-content:center;z-index:2}
.hero-arrow.left{left:0}.hero-arrow.right{right:0}
.hero-curve{position:absolute;top:580px;left:0;width:1200px;height:90px;z-index:2}
.scroll-btn{position:absolute;top:610px;left:578px;width:44px;height:44px;border-radius:50%;background:var(--white);box-shadow:0 2px 8px rgba(0,0,0,.2);display:flex;align-items:center;justify-content:center;z-index:3}

/* features */
.features{top:730px;height:170px;display:flex;justify-content:space-between}
.feature{width:220px;text-align:left}
.feature svg{width:54px;height:54px;margin-left:18px}
.feature p{margin-top:22px;font-size:15px;font-weight:500}
.divider{top:940px;height:1px;background:var(--line)}

/* about */
.about-photo{position:absolute;top:1048px;left:100px;width:440px;height:384px;background:linear-gradient(135deg,#d7dde0,#a9b4bb 60%,#e9ecee)}
.about-badge{position:absolute;top:1370px;left:486px;width:84px;height:84px;border-radius:50%;background:var(--blue);border:5px solid var(--white);display:flex;align-items:center;justify-content:center}
.about-text{position:absolute;top:1040px;left:580px;width:520px}
.eyebrow{font-size:12px;font-weight:600;color:var(--green);letter-spacing:1px;text-transform:uppercase}
.about-text h2{font-size:22px;font-weight:600;color:var(--blue);margin:6px 0 26px}
.about-text p{font-size:12.5px;line-height:1.75;color:var(--muted);margin-bottom:14px}

/* contact */
.contact{position:absolute;top:1520px;left:0;width:1200px;height:500px;background:linear-gradient(120deg,#00a990 0%,#33b8a4 55%,#00a990 100%);overflow:hidden}
.contact h2{position:absolute;top:48px;width:1200px;text-align:center;font-size:24px;font-weight:600;color:var(--white)}
.form{position:absolute;top:118px;left:232px;width:736px}
.form-row{display:flex;gap:16px}
.field{flex:1}
.field label{display:block;font-size:12px;color:var(--white);margin-bottom:6px}
.field .input{height:40px;background:var(--white);border-radius:2px;font-size:11px;color:#9aa0a8;padding:12px}
.field .textarea{height:110px}
.form-row+.form-row{margin-top:22px}
.submit{position:absolute;top:392px;left:544px;width:112px;height:44px;background:var(--white);border:2px solid var(--ink);font-size:13px;font-weight:600;text-align:center;line-height:40px}

/* customers */
.customers{top:2048px}
.customers .eyebrow,.customers h2{text-align:center}
.customers h2{font-size:26px;font-weight:600;margin-top:4px}
.car-arrows{position:absolute;top:88px;right:0;display:flex;gap:6px}
.car-arrows div{width:30px;height:30px;display:flex;align-items:center;justify-content:center;background:#eef0f2}
.car-arrows div.on{background:var(--green)}
.logo-row{position:absolute;top:196px;left:0;width:1000px;display:flex;gap:16px}
.logo-box{flex:1;height:76px;border:1px solid var(--line);display:flex;align-items:center;justify-content:center;font-size:18px;font-weight:600;color:#8a9098}
.logo-box.hl{border-color:var(--green);box-shadow:0 3px 10px rgba(0,0,0,.12)}

/* address */
.address{top:2476px}
.address .eyebrow,.address h2{text-align:center}
.address h2{font-size:28px;font-weight:600;margin-top:4px}
.addr-cols{position:absolute;top:150px;left:0;width:1000px;display:flex;justify-content:space-between}
.addr-col{width:240px;text-align:center}
.addr-col svg{width:30px;height:30px;fill:var(--blue)}
.addr-col h3{font-size:14px;font-weight:600;margin:12px 0 6px;letter-spacing:.5px}
.addr-col p{font-size:12.5px;color:var(--muted);line-height:1.5}
.addr-col:first-child{text-align:left;width:200px}
.addr-col:first-child svg,.addr-col:first-child h3{margin-left:70px}
.addr-col:first-child h3{margin-left:44px}

/* footer */
.footer{position:absolute;top:2820px;left:0;width:1200px;height:240px;background:var(--blue);color:var(--white)}
.footer .brand{top:60px}
.footer .brand-name{color:var(--white)}
.footer .brand-square{background:var(--white)}
.footer-nav{position:absolute;top:78px;right:100px;display:flex;gap:32px;font-size:12px;font-weight:500}
.footer-line{position:absolute;top:150px;left:100px;width:1000px;height:1px;background:rgba(255,255,255,.3)}
.copyright{position:absolute;top:180px;width:1200px;text-align:center;font-size:11px;color:rgba(255,255,255,.8);letter-spacing:.5px}
</style>
</head>
<body>

<header class="topbar">
  <div class="brand"><span class="brand-square"></span><span class="brand-name">Kolrith</span></div>
  <div class="contact-strip">
    <span><svg viewBox="0 0 24 24"><path d="M6.6 10.8a15 15 0 0 0 6.6 6.6l2.2-2.2c.3-.3.7-.4 1-.2 1.1.4 2.3.6 3.6.6.6 0 1 .4 1 1V20c0 .6-.4 1-1 1A17 17 0 0 1 3 4c0-.6.4-1 1-1h3.5c.6 0 1 .4 1 1 0 1.3.2 2.5.6 3.6.1.3 0 .7-.2 1z"/></svg>(852) 3018 4420</span>
    <span><svg viewBox="0 0 24 24"><path d="M2 5h20v14H2zm2 2v.5l8 5 8-5V7l-8 5z"/></svg>sales@kolrithpanel.com</span>
    <span><i class="lang-dot"></i>EN</span>
  </div>
</header>

<div class="hero" role="img" aria-label="Photo of a bright factory corridor with glass partitions"></div>
<nav class="navbar">
  <a class="active">HOME</a><a>PRODUCTS</a><a>OUR FACILITIES</a><a>CUSTOMERS</a><a>NEWS</a><a>QUOTES</a><a>CONTACT US</a>
  <a class="quote">ONLINE QUOTE</a>
</nav>
<div class="hero-arrow left"><svg width="12" height="12" viewBox="0 0 12 12"><path d="M8 1 3 6l5 5" stroke="#333" stroke-width="2" fill="none"/></svg></div>
<div class="hero-arrow right"><svg width="12" height="12" viewBox="0 0 12 12"><path d="M4 1l5 5-5 5" stroke="#333" stroke-width="2" fill="none"/></svg></div>
<h1 class="hero-title">Our Printed Circuit Board<br>Business Is Committed To Excellence</h1>
<svg class="hero-curve" viewBox="0 0 1200 90" preserveAspectRatio="none"><path d="M0 0 Q600 110 1200 0 V90 H0 Z" fill="#fff"/></svg>
<div class="scroll-btn"><svg width="14" height="14" viewBox="0 0 14 14"><path d="M7 1v11M2 7l5 5 5-5" stroke="#333" stroke-width="2" fill="none"/></svg></div>

<section class="wrap features">
  <div class="feature">
    <svg viewBox="0 0 54 54"><circle cx="27" cy="20" r="14" fill="none" stroke="#0353a1" stroke-width="4"/><circle cx="27" cy="20" r="6" fill="#0353a1"/><path d="M18 31l-5 18 8-4 4 7 4-14M36 31l5 18-8-4-4 7" fill="#0353a1"/></svg>
    <p>Excellence In Quality</p>
  </div>
  <div class="feature">
    <svg viewBox="0 0 54 54"><rect x="4" y="30" width="10" height="18" fill="#0353a1"/><path d="M16 32h12l8 4h10c3 0 3 5 0 5H30v3h18l4-4v8H16z" fill="#0353a1"/><circle cx="34" cy="14" r="10" fill="none" stroke="#0353a1" stroke-width="3.5"/><path d="M34 8v12" stroke="#0353a1" stroke-width="3"/></svg>
    <p>Excellence In Price</p>
  </div>
  <div class="feature">
    <svg viewBox="0 0 54 54"><circle cx="27" cy="27" r="9" fill="#fff" stroke="#0353a1" stroke-width="5"/><path d="M27 4v8M27 42v8M4 27h8M42 27h8M11 11l6 6M37 37l6 6M43 11l-6 6M17 37l-6 6" stroke="#0353a1" stroke-width="7"/><circle cx="27" cy="27" r="16" fill="none" stroke="#0353a1" stroke-width="6"/></svg>
    <p>Excellence In Service</p>
  </div>
  <div class="feature">
    <svg viewBox="0 0 54 54"><rect x="2" y="12" width="32" height="26" fill="#0353a1"/><path d="M36 20h9l7 9v9H36z" fill="#0353a1"/><circle cx="12" cy="42" r="5" fill="#0353a1" stroke="#fff" stroke-width="2"/><circle cx="44" cy="42" r="5" fill="#0353a1" stroke="#fff" stroke-width="2"/></svg>
    <p>Excellence In On Time Delivery</p>
  </div>
</section>
<div class="wrap divider"></div>

<div class="about-photo" role="img" aria-label="Photo of a technician operating PCB production equipment"></div>
<div class="about-badge"><svg width="36" height="36" viewBox="0 0 36 36"><path d="M3 16l8-7 7 4 7-4 8 7-9 10-6-5-6 5z" fill="none" stroke="#fff" stroke-width="2.5" stroke-linejoin="round"/></svg></div>
<section class="about-text">
  <p class="eyebrow">Welcome To</p>
  <h2>Kolrith Global Limited (KGL)</h2>
  <p>Established in 1991, Kolrith Global Limited (KGL) is a strong and growing company specialising in single and double sided printed circuit boards. Its manufacturing facility is located in a self owned factory in Yongjiang, Dongguan, within easy reach of Hong Kong.</p>
  <p>Our focus is to be a precision low cost PCB partner of our customers, meeting their requirements in large quantity production as well as high mix low volume part numbers.</p>
  <p>Through our steadfast drive for lean efficiency, KGL is becoming a highly efficient PCB factory with an output of more than 100,000 square meters per month and we aim at reaching 150,000 square meters by the end of 2018.</p>
  <p>KGL is our business and it is through continued automation and innovation that will drive our growth in the next 10 years.</p>
</section>

<section class="contact">
  <h2>Get In Touch With Us</h2>
  <div class="form">
    <div class="form-row">
      <div class="field"><label>Name*</label><div class="input">Enter your name</div></div>
      <div class="field"><label>Email*</label><div class="input">Enter your email</div></div>
      <div class="field"><label>Company*</label><div class="input">Enter your name</div></div>
    </div>
    <div class="form-row">
      <div class="field"><label>Comments*</label><div class="input textarea">Enter your comments</div></div>
    </div>
  </div>
  <div class="submit">SUBMIT</div>
</section>

<section class="wrap customers">
  <p class="eyebrow">Kolrith Board</p>
  <h2>Our Customer</h2>
  <div class="car-arrows">
    <div><svg width="10" height="10" viewBox="0 0 10 10"><path d="M7 1 3 5l4 4" stroke="#333" stroke-width="2" fill="none"/></svg></div>
    <div class="on"><svg width="10" height="10" viewBox="0 0 10 10"><path d="M3 1l4 4-4 4" stroke="#fff" stroke-width="2" fill="none"/></svg></div>
  </div>
  <div class="logo-row">
    <div class="logo-box">Veltra</div>
    <div class="logo-box">Norvane</div>
    <div class="logo-box hl">Solvik</div>
    <div class="logo-box">Tessaro</div>
    <div class="logo-box">Makon</div>
    <div class="logo-box">Arvelo</div>
  </div>
</section>

<section class="wrap address">
  <p class="eyebrow">Business Address Is As Follows</p>
  <h2>Hong Kong</h2>
  <div class="addr-cols">
    <div class="addr-col">
      <svg viewBox="0 0 24 24"><path d="M12 2a7 7 0 0 0-7 7c0 5 7 13 7 13s7-8 7-13a7 7 0 0 0-7-7zm0 9.5A2.5 2.5 0 1 1 12 6.5a2.5 2.5 0 0 1 0 5z"/></svg>
      <h3>ADDRESS</h3>
      <p>Kolrith Global Limited<br>18/F Harbourline Tower 42 Marlow Road<br>Causeway Bay Hong Kong</p>
    </div>
    <div class="addr-col">
      <svg viewBox="0 0 24 24"><path d="M6.6 10.8a15 15 0 0 0 6.6 6.6l2.2-2.2c.3-.3.7-.4 1-.2 1.1.4 2.3.6 3.6.6.6 0 1 .4 1 1V20c0 .6-.4 1-1 1A17 17 0 0 1 3 4c0-.6.4-1 1-1h3.5c.6 0 1 .4 1 1 0 1.3.2 2.5.6 3.6.1.3 0 .7-.2 1z"/></svg>
      <h3>PHONE</h3>
      <p>+852-3018 4420</p>
    </div>
    <div class="addr-col">
      <svg viewBox="0 0 24 24"><path d="M6 2h10v5H6zM4 9h16a2 2 0 0 1 2 2v7h-4v4H6v-4H2v-7a2 2 0 0 1 2-2zm4 8v3h8v-3z"/></svg>
      <h3>FAX</h3>
      <p>852-3018 4421</p>
    </div>
    <div class="addr-col">
      <svg viewBox="0 0 24 24"><path d="M2 5h20v14H2zm2 2v.5l8 5 8-5V7l-8 5z"/></svg>
      <h3>EMAIL</h3>
      <p>sales@kolrithpanel.com</p>
    </div>
  </div>
</section>

<footer class="footer">
  <div class="brand"><span class="brand-square"></span><span class="brand-name">Kolrith</span></div>
  <nav class="footer-nav"><span>HOME</span><span>PRODUCTS</span><span>OUR FACILITIES</span><span>CUSTOMERS</span><span>NEWS</span><span>QUOTES</span><span>CONTACT US</span></nav>
  <div class="footer-line"></div>
  <p class="copyright">COPYRIGHT © 2018 KOLRITH GLOBAL LIMITED. ALL RIGHTS RESERVED</p>
</footer>

</body>
</html>
```